WILLOWMERE PERK WEBSITE HOME PAGE AND CHECKOUT PAGES

UPDATE TO BRIEF:

Willowmere Perks is a company that provides Charities with the Free Vacation Vouchers that they can use to incentivize people to donate which in turn increases donations for the chairty.

So I need to keep it a little more template like the example url I gave. http://plinthframes.com/willowmere-perk/ Because, I am going to provide template to ANY CHARITY TYPE and they just fill in the content into the template and change images or whatever for their charity. So I am really looking for a website template that can be used for multiple and different kinds of charities.

So where the logo would go please use YOUR LOGO HERE generic logo for now

and where ever you promote the Free Vacation Certificate To Las Vegas please add "Brought To You By" (logo willowmere perks or something...basically its a partnership with the Charity and Willowmere Perk)

So Willowmere Perk is a marketing company and not a Charity but more of a plug and play platform that allows a charity to accepts donations and immediately deliver the promised incentive offer after donation is made on the website.

When a Charity is able to offer a high perceived value gift for a donation they increase donations.

Target Market(s)

PEOPLE THAT DONATE TO CHARITIES

Industry/Entity Type

Charity

Number of Pages Required

3 page

Requirements
Must have
• One thing i need to add to the website is an Incentive Gift for the Donation.

So I need this tagline and images to make the promotion seem great:
"Donate $100 and Receive A Free 3 Night Vacation Certificate To Las Vegas!"

Maybe show image of vegas or some kind of nice graphic that promotes the vegas vacation as a gift for the $100 donation very well"

I need the payment pages as well. So when someone click Donate Now, the next page is there where they can see their gift that is included with the donation, and also the donation amount...
Nice to have

Should not have

```html
<!DOCTYPE html>
<html lang="en">
<head>
<meta charset="utf-8">
<title>Willowmere Perk</title>
<link href="https://fonts.googleapis.com/css2?family=Montserrat:wght@600;700;800&family=Open+Sans:wght@400;600;700&family=Merriweather:wght@700&display=swap" rel="stylesheet">
<style>
:root{
  --cyan:#14b4e2;
  --cyan-dark:#0e9cc6;
  --ink:#2b2b2b;
  --text:#6f6f6f;
  --muted:#8a8a8a;
  --light:#f2f3f4;
  --dark:#1d1f21;
  --white:#ffffff;
  --line:#e2e2e2;
}
*{box-sizing:border-box;margin:0;padding:0}
html,body{width:1200px;height:3600px;overflow:hidden}
body{position:relative;background:var(--white);font-family:"Open Sans",Arial,sans-serif;color:var(--text)}
.abs{position:absolute}
.section-title{position:absolute;left:0;width:1200px;text-align:center;font-family:"Montserrat",Arial,sans-serif;font-weight:700;font-size:18px;letter-spacing:2px;color:var(--ink)}
.section-title .hl{color:var(--cyan)}
.section-title::after{content:"";display:block;width:42px;height:2px;background:var(--cyan);margin:8px auto 0}
.section-sub{position:absolute;left:150px;width:900px;text-align:center;font-size:11px;line-height:14px;letter-spacing:.5px;color:var(--muted)}
.dark .section-title{color:var(--white)}
.dark .section-sub{color:#ddd}

/* header */
.logo-card{left:163px;top:0;width:218px;height:83px;background:var(--white);box-shadow:0 3px 8px rgba(0,0,0,.25);border-radius:0 0 4px 4px;display:flex;align-items:center;padding-left:14px;gap:9px;z-index:3}
.logo-mark{width:30px;height:30px;background:var(--cyan);border-radius:4px;flex:none}
.logo-name{font-family:"Montserrat",Arial,sans-serif;font-weight:700;font-size:18px;line-height:20px;color:var(--cyan-dark)}
.navbar{left:381px;top:0;width:657px;height:52px;background:var(--white);display:flex;align-items:center;padding-left:102px;font-size:10px;letter-spacing:.8px;color:#555;z-index:2}
.navbar span.sep{margin:0 9px;color:#999}
.navbar .active{color:var(--cyan)}
.btn-pill{display:inline-block;background:var(--cyan);color:var(--white);font-weight:700;font-size:10px;letter-spacing:1px;border-radius:14px;text-align:center}
.navbar .btn-pill{margin-left:auto;margin-right:14px;padding:7px 13px}

/* hero */
.hero{left:0;top:0;width:1200px;height:560px;background:radial-gradient(ellipse at 50% 35%,#2c3346 0%,#161a26 45%,#07080d 100%)}
.hero-glow{left:0;top:260px;width:1200px;height:300px;background:linear-gradient(180deg,rgba(0,0,0,0) 0%,rgba(120,80,30,.35) 60%,rgba(60,40,20,.4) 100%)}
.hero-curve{left:0;top:490px}
.hero-title{left:0;top:216px;width:1200px;text-align:center;font-family:"Montserrat",Arial,sans-serif;font-weight:800;font-size:54px;line-height:64px;letter-spacing:3px;color:var(--cyan);white-space:nowrap}
.hero-sub{left:0;top:283px;width:1200px;text-align:center;font-family:"Montserrat",Arial,sans-serif;font-weight:700;font-size:16px;line-height:21px;letter-spacing:1.2px;color:var(--white)}
.hero-sub .hl{color:var(--cyan)}
.hero-btn{left:536px;top:347px;width:128px;height:28px;line-height:28px}

.promo-card{top:495px;width:270px;height:180px;background:linear-gradient(135deg,#8b8f94,#5d6166);}
.promo-card::before{content:"";position:absolute;inset:0;background:rgba(40,40,40,.45)}
.promo-frame{position:absolute;left:8px;top:8px;right:8px;bottom:8px;border:1px solid rgba(255,255,255,.8);text-align:center;color:var(--white)}
.promo-icon{width:58px;height:58px;background:var(--white);border-radius:6px;margin:5px auto 0;display:flex;align-items:center;justify-content:center}
.promo-frame h3{font-family:"Montserrat",Arial,sans-serif;font-weight:700;font-size:15px;margin-top:11px}
.promo-frame p{font-size:9px;line-height:11px;margin:9px 14px 0}

/* about */
.about{left:0;top:710px;width:1200px;height:313px;background:var(--light)}
.about-photo-a{left:163px;top:776px;width:256px;height:196px;background:linear-gradient(135deg,#7c9a64,#a8aaa7 60%,#6f8c5c)}
.about-photo-b{left:370px;top:870px;width:170px;height:128px;border:6px solid var(--white);background:linear-gradient(135deg,#c99f78,#e9e3c8)}
.about-text{left:566px;top:784px;width:472px;font-size:10.5px;line-height:16.5px;color:var(--muted)}
.about-text .hl{color:var(--cyan);font-weight:600;font-size:12px}
.about-text p+p{margin-top:10px}
.about-list{left:566px;top:967px;width:472px;display:grid;grid-template-columns:1fr 1fr;row-gap:4px;font-size:10.5px;color:var(--muted)}
.about-list li{list-style:none;display:flex;align-items:center;gap:7px}
.diamond{width:7px;height:7px;border:1.5px solid var(--cyan);transform:rotate(45deg)}

/* causes */
.cause-card{top:1146px;width:269px;height:306px;background:var(--white);box-shadow:0 1px 5px rgba(0,0,0,.2)}
.cause-img{height:154px;margin:3px 3px 0}
.cause-body{padding:10px 14px 0}
.cause-tag{font-size:10.5px;color:var(--cyan)}
.cause-title{font-family:"Montserrat",Arial,sans-serif;font-weight:600;font-size:11px;line-height:13px;color:var(--ink);margin-top:6px;height:28px}
.cause-stats{display:flex;justify-content:space-between;margin-top:12px}
.cause-stats b{display:block;font-family:"Montserrat",Arial,sans-serif;font-size:14px;color:var(--ink)}
.cause-stats small{font-size:10px;color:var(--muted)}
.cause-stats div:last-child{text-align:right}
.cause-foot{border-top:1px solid var(--line);margin:10px 14px 0;padding-top:9px;display:flex;align-items:center;gap:8px;font-size:9px;color:#555}
.avatar{width:24px;height:24px;border-radius:50%;background:#cfe9f4}
.cause-foot span{color:var(--cyan)}
.arrow-box{width:26px;height:24px;border:1.5px solid var(--cyan);display:flex;align-items:center;justify-content:center}

/* gallery */
.g-tile{width:294px;height:168px}
.g-overlay{background:#1a1a1a}
.g-overlay .inner{position:absolute;left:8px;top:8px;right:8px;bottom:8px;border:1px solid rgba(255,255,255,.8);text-align:center;color:var(--white)}
.g-overlay h4{font-family:"Montserrat",Arial,sans-serif;font-size:14px;margin-top:44px}
.g-overlay .icons{display:flex;justify-content:center;gap:10px;margin-top:14px}
.ring{width:25px;height:25px;border:1px solid var(--white);border-radius:50%;display:flex;align-items:center;justify-content:center}

/* testimonials */
.testi{left:0;top:1992px;width:1200px;height:362px;background:linear-gradient(135deg,#2a302c,#1d211e 60%,#2c2f2a)}
.testi::before{content:"";position:absolute;inset:0;background:rgba(0,0,0,.55)}
.t-card{top:2125px;width:259px;height:151px;background:var(--white);text-align:center}
.t-quote{position:absolute;left:106px;top:-24px;width:46px;height:46px;border-radius:50%;background:var(--cyan);color:var(--white);font-family:"Merriweather",Georgia,serif;font-size:34px;line-height:58px}
.t-card p{font-size:11px;line-height:16px;color:#666;margin:34px 14px 0}
.t-name{font-family:"Merriweather",Georgia,serif;font-weight:700;font-size:12px;color:var(--ink);margin-top:14px}
.t-role{font-size:9px;font-style:italic;color:#777;margin-top:2px}
.dots{left:582px;top:2314px;display:flex;gap:5px}
.dots i{width:8px;height:8px;border-radius:50%;border:1.5px solid var(--cyan)}
.dots i.on{background:var(--cyan)}

/* news */
.news{top:2473px;width:268px}
.news-img{height:142px}
.news-row{display:flex;gap:12px;margin-top:14px}
.news-row h4{font-family:"Montserrat",Arial,sans-serif;font-weight:600;font-size:12px;line-height:14px;color:var(--ink)}
.news-row p{font-size:9px;line-height:13px;color:var(--muted);margin-top:5px}
.news-row a{display:block;font-size:9px;font-weight:700;color:var(--cyan);margin-top:8px;text-decoration:none}
.date{flex:none;width:60px;margin-top:-2px}
.date .d{background:#3a3d41;color:var(--white);font-family:"Merriweather",Georgia,serif;font-size:11.5px;text-align:center;height:26px;line-height:26px}
.date .c{background:var(--cyan);color:var(--white);font-weight:700;font-size:13px;height:26px;display:flex;align-items:center;justify-content:center;gap:4px}

/* partners */
.partner{top:2827px;width:196px;height:81px;border:1px solid var(--line);display:flex;align-items:center;justify-content:center}
.partner i{width:96px;height:18px;background:#d8d8d8;border-radius:3px}
.p-arrow{top:2926px;width:26px;height:24px;border:1.5px solid #333;display:flex;align-items:center;justify-content:center}

/* contact */
.ask{left:0;top:2990px;width:1200px;height:345px;background:linear-gradient(135deg,#2d342d,#1b1f1c 55%,#2a2d28)}
.ask::before{content:"";position:absolute;inset:0;background:rgba(0,0,0,.55)}
.field{width:240px;height:31px;border:1px solid #777;border-radius:2px;font-size:10.5px;letter-spacing:.5px;color:#ccc;padding:8px 12px}
.field.wide{width:495px;height:84px}
.submit{left:560px;top:3314px;width:88px;height:28px;line-height:28px;background:var(--cyan);color:var(--white);font-family:"Montserrat",Arial,sans-serif;font-weight:700;font-size:12px;letter-spacing:1.5px;text-align:center;z-index:2}

/* footer */
.footer{left:0;top:3335px;width:1200px;height:219px;background:var(--cyan);color:var(--white)}
.f-logo{left:504px;top:3350px;display:flex;align-items:center;gap:9px}
.f-logo .logo-mark{background:var(--white)}
.f-logo .logo-name{color:var(--white)}
.f-links{left:0;top:3408px;width:1200px;text-align:center;font-size:11px;letter-spacing:.5px;color:var(--white)}
.f-links .sep{margin:0 10px}
.f-info{top:3436px;text-align:center;font-size:10px;line-height:15px;color:var(--white)}
.f-info svg{display:block;margin:0 auto 7px}
.f-bottom{left:434px;top:3506px;display:flex;gap:12px;align-items:center}
.mail-pill{height:28px;border:1px solid var(--white);border-radius:14px;padding:0 14px;display:flex;align-items:center;gap:6px;font-size:10px;color:var(--white)}
.soc{width:28px;height:28px;border:1px solid var(--white);border-radius:50%;display:flex;align-items:center;justify-content:center}
.soc i{width:8px;height:8px;background:var(--white);border-radius:50%}
.copy{left:0;top:3554px;width:1200px;height:46px;line-height:46px;background:#3b3d40;text-align:center;color:var(--white);font-size:11px;letter-spacing:.6px}
</style>
</head>
<body>

<!-- HERO -->
<div class="abs hero" role="img" aria-label="Night skyline of Las Vegas with city lights"></div>
<div class="abs hero-glow"></div>
<svg class="abs hero-curve" width="1200" height="72" viewBox="0 0 1200 72"><path d="M0 20 Q600 -5 1200 20 L1200 72 L0 72 Z" fill="#ffffff"/></svg>

<div class="abs logo-card"><span class="logo-mark"></span><span class="logo-name">Willowmere<br>Perks</span></div>
<nav class="abs navbar">
  <span class="active">HOME</span><span class="sep">/</span><span>ABOUT US</span><span class="sep">/</span><span>CAUSES</span><span class="sep">/</span><span>EVENT</span><span class="sep">/</span><span>BLOG</span><span class="sep">/</span><span>CONTACT US</span>
  <span class="btn-pill">DONATE NOW</span>
</nav>

<h1 class="abs hero-title">Willowmere Perk</h1>
<p class="abs hero-sub">Donate $100 and Receive A Free<br>3 Night Vacation Certificate To <span class="hl">Las Vegas!</span></p>
<span class="abs btn-pill hero-btn">DONATE NOW</span>

<div class="abs promo-card" style="left:174px" role="img" aria-label="Medical care photo">
  <div class="promo-frame">
    <div class="promo-icon"><svg width="36" height="36" viewBox="0 0 36 36" fill="none" stroke="#14b4e2" stroke-width="2"><path d="M4 24l8-6h8l6 3-2 3h-8"/><path d="M10 30l10-2 12-8"/><rect x="17" y="6" width="12" height="12" rx="2" transform="rotate(30 23 12)"/></svg></div>
    <h3>Medical Care Donate</h3>
    <p>But I must explain to you how all this mistaken idea of denouncing pleasure and praising pain was born and I will give you a complete account...</p>
  </div>
</div>
<div class="abs promo-card" style="left:465px" role="img" aria-label="Child education photo">
  <div class="promo-frame">
    <div class="promo-icon"><svg width="36" height="36" viewBox="0 0 36 36" fill="none" stroke="#14b4e2" stroke-width="2"><path d="M4 10h12a2 2 0 012 2v18a2 2 0 00-2-2H4z"/><path d="M32 10H20a2 2 0 00-2 2v18a2 2 0 012-2h12z"/><path d="M8 15h6M8 19h6M22 15h6M22 19h6"/></svg></div>
    <h3>Child Education Donate</h3>
    <p>But I must explain to you how all this mistaken idea of denouncing pleasure and praising pain was born and I will give you a complete account...</p>
  </div>
</div>
<div class="abs promo-card" style="left:756px" role="img" aria-label="Money donation photo">
  <div class="promo-frame">
    <div class="promo-icon"><svg width="36" height="36" viewBox="0 0 36 36" fill="none" stroke="#14b4e2" stroke-width="2"><circle cx="22" cy="11" r="7"/><path d="M22 8v6"/><path d="M3 26l7-5h8l5 2-2 3h-7"/><path d="M8 32l11-2 13-8"/></svg></div>
    <h3>Money Donate</h3>
    <p>But I must explain to you how all this mistaken idea of denouncing pleasure and praising pain was born and I will give you a complete account...</p>
  </div>
</div>

<!-- ABOUT -->
<section class="abs about"></section>
<h2 class="section-title" style="top:732px"><span class="hl">ABOUT WILLOWMERE</span> PERK</h2>
<div class="abs about-photo-a" role="img" aria-label="Group of volunteers in a park"></div>
<div class="abs about-photo-b" role="img" aria-label="Young child at a table"></div>
<div class="abs about-text">
  <p><span class="hl">Willowmere Perks</span> Sed ut perspiciatis unde omnis iste natus error sit voluptatem accusantium doloremque laudantium, totam rem aperiam, eaque ipsa quae ab illo inventore veritatis et quasi architecto beatae vitae dicta sunt explicabo. Nemo enim ipsam voluptatem quia voluptas sit aspernatur aut odit aut fugit, sed quia consequuntur magni dolores eos qui ratione voluptatem sequi nesciunt.</p>
  <p>But I must explain to you how all this mistaken idea of denouncing pleasure and praising pain was born and I will give you a complete account of the system, and expound the actual teachings of the great explorer of the truth, the master-builder of human happiness.</p>
</div>
<ul class="abs about-list">
  <li><i class="diamond"></i>Children's Charities.</li>
  <li><i class="diamond"></i>Human Care Charities.</li>
  <li><i class="diamond"></i>Women, Children &amp; Family Charities.</li>
  <li><i class="diamond"></i>Children's Medical Charities.</li>
</ul>

<!-- CAUSES -->
<h2 class="section-title" style="top:1062px"><span class="hl">POPULAR</span> CAUSES</h2>
<p class="section-sub" style="top:1103px">Sed ut perspiciatis unde omnis iste natus error sit voluptatem accusantium doloremque laudantium, totam rem aperiam, eaque ipsa quae ab illo inventore veritatis et quasi architecto beatae vitae dicta sunt explicabo.</p>

<div class="abs arrow-box" style="left:137px;top:1287px"><svg width="14" height="10" viewBox="0 0 14 10" fill="none" stroke="#14b4e2" stroke-width="1.8"><path d="M13 5H1M5 1L1 5l4 4"/></svg></div>
<div class="abs arrow-box" style="left:1037px;top:1287px"><svg width="14" height="10" viewBox="0 0 14 10" fill="none" stroke="#14b4e2" stroke-width="1.8"><path d="M1 5h12M9 1l4 4-4 4"/></svg></div>

<article class="abs cause-card" style="left:174px">
  <div class="cause-img" style="background:linear-gradient(135deg,#5d4a3c,#c9a98a 60%,#e0c7a6)" role="img" aria-label="Smiling schoolchildren in a classroom"></div>
  <div class="cause-body">
    <div class="cause-tag">Education</div>
    <div class="cause-title">Lorem ipsum dolor sit amet, consectetur adipiscing elit, sed</div>
    <div class="cause-stats"><div><b>$300</b><small>Goal</small></div><div><b>$350</b><small>Pledged</small></div></div>
  </div>
  <div class="cause-foot"><i class="avatar"></i>By <span>Hearthsong</span></div>
</article>
<article class="abs cause-card" style="left:465px">
  <div class="cause-img" style="background:linear-gradient(135deg,#d9c9a4,#eef0f0 60%,#cfd8dc)" role="img" aria-label="Child at a medical check-up"></div>
  <div class="cause-body">
    <div class="cause-tag">Medical</div>
    <div class="cause-title">Sed ut perspiciatis unde omnis iste natus error sit voluptatem</div>
    <div class="cause-stats"><div><b>$200</b><small>Goal</small></div><div><b>$300</b><small>Pledged</small></div></div>
  </div>
  <div class="cause-foot"><i class="avatar"></i>By <span>Hearthsong</span></div>
</article>
<article class="abs cause-card" style="left:755px">
  <div class="cause-img" style="background:linear-gradient(135deg,#c84848,#e7a0b0 50%,#5a8a5a)" role="img" aria-label="Group of children at a festive activity"></div>
  <div class="cause-body">
    <div class="cause-tag">children activity</div>
    <div class="cause-title">Lorem ipsum dolor sit amet, consectetur adipiscing elit, sed do eiusmod tempor</div>
    <div class="cause-stats"><div><b>$150</b><small>Goal</small></div><div><b>$200</b><small>Pledged</small></div></div>
  </div>
  <div class="cause-foot"><i class="avatar"></i>By <span>Hearthsong</span></div>
</article>

<!-- GALLERY -->
<h2 class="section-title" style="top:1506px"><span class="hl">OUR</span> GALLERY</h2>
<p class="section-sub" style="top:1550px">Sed cursus elementum arcu vitae mollis. Curabitur vehicula egestas libero.</p>

<div class="abs g-tile" style="left:0;top:1587px;background:linear-gradient(135deg,#4d7a3c,#8fb56a 50%,#3f5fa0)" role="img" aria-label="Volunteers planting in a park"></div>
<div class="abs g-tile g-overlay" style="left:302px;top:1587px">
  <div class="inner"><h4>Sed ut perspiciatis unde omnis</h4>
    <div class="icons">
      <span class="ring"><svg width="11" height="11" viewBox="0 0 12 12" fill="none" stroke="#fff" stroke-width="1.6"><circle cx="5" cy="5" r="3.5"/><path d="M8 8l3 3"/></svg></span>
      <span class="ring"><svg width="11" height="11" viewBox="0 0 12 12" fill="none" stroke="#fff" stroke-width="1.6"><path d="M5 7l2-2M4 6L2.5 7.5a2 2 0 003 3L7 9M8 6l1.5-1.5a2 2 0 00-3-3L5 3"/></svg></span>
    </div>
  </div>
</div>
<div class="abs g-tile" style="left:604px;top:1587px;background:linear-gradient(135deg,#d14a4a,#f0a6c0 50%,#6a9b5e)" role="img" aria-label="Children celebrating together"></div>
<div class="abs g-tile" style="left:906px;top:1587px;background:linear-gradient(135deg,#e8e6df,#cbb28f 60%,#c4c39a)" role="img" aria-label="Young child receiving food"></div>
<div class="abs g-tile" style="left:0;top:1762px;background:linear-gradient(135deg,#3a2a22,#8a6a58 60%,#b9a595)" role="img" aria-label="Child drinking from a water tap"></div>
<div class="abs g-tile" style="left:302px;top:1762px;background:linear-gradient(135deg,#6a5540,#a7886a 60%,#d7c3a4)" role="img" aria-label="Two children at a desk"></div>
<div class="abs g-tile" style="left:604px;top:1762px;background:linear-gradient(135deg,#4f7a3a,#6d5a48 50%,#a8694a)" role="img" aria-label="Outdoor classroom"></div>
<div class="abs g-tile" style="left:906px;top:1762px;background:linear-gradient(135deg,#7c9a64,#a8aaa7 60%,#6f8c5c)" role="img" aria-label="Group of volunteers in a park"></div>

<!-- TESTIMONIALS -->
<section class="abs testi" role="img" aria-label="Volunteers background photo, darkened"></section>
<div class="dark">
  <h2 class="section-title" style="top:2025px"><span class="hl">OUR</span> TESTIMONIALS</h2>
  <p class="section-sub" style="top:2068px">Sed cursus elementum arcu vitae mollis. Curabitur vehicula egestas libero.</p>
</div>
<div class="abs t-card" style="left:174px"><span class="t-quote">&ldquo;</span><p>Lorem ipsum dolor sit amet, consectetur adipiscing elit, sed do eiusmod tempor incididunt ut labore.</p><div class="t-name">Dana Holloway</div><div class="t-role">Chicago, IL</div></div>
<div class="abs t-card" style="left:470px"><span class="t-quote">&ldquo;</span><p>Lorem ipsum dolor sit amet, consectetur adipiscing elit, sed do eiusmod tempor incididunt ut labore.</p><div class="t-name">Pieter Lund</div><div class="t-role">Patient Of Asthama</div></div>
<div class="abs t-card" style="left:766px"><span class="t-quote">&ldquo;</span><p>Lorem ipsum dolor sit amet, consectetur adipiscing elit, sed do eiusmod tempor incididunt ut labore.</p><div class="t-name">Marco Vellani</div><div class="t-role">Chicago, IL</div></div>
<div class="abs dots"><i></i><i class="on"></i><i></i></div>

<!-- NEWS -->
<h2 class="section-title" style="top:2402px"><span class="hl">LATEST</span> NEWS</h2>
<p class="section-sub" style="top:2443px">Sed cursus elementum arcu vitae mollis curabitur</p>

<article class="abs news" style="left:173px">
  <div class="news-img" style="background:linear-gradient(135deg,#1aa0c8,#4cc3e0 60%,#2b8fb0)" role="img" aria-label="Child drinking from a tap, blue tint"></div>
  <div class="news-row"><div><h4>Sed ut perspiciatis unde omnis iste natus</h4><p>Lorem ipsum dolor sit amet, consectetur adipiscing elit, sed do eiusmod tempor incididunt ut labore et dolore magna aliqua.</p><a>Read More</a></div>
  <div class="date"><div class="d">15 OCT</div><div class="c"><svg width="12" height="10" viewBox="0 0 12 10" fill="none" stroke="#fff" stroke-width="1.5"><path d="M1 5a5 4 0 1110 0 5 4 0 01-7 3.5L1 9.5z"/></svg>0</div></div></div>
</article>
<article class="abs news" style="left:464px">
  <div class="news-img" style="background:linear-gradient(135deg,#e8e6df,#cbb28f 60%,#c4c39a)" role="img" aria-label="Young child receiving food"></div>
  <div class="news-row"><div><h4>Sed ut perspiciatis unde omnis iste natus</h4><p>Lorem ipsum dolor sit amet, consectetur adipiscing elit, sed do eiusmod tempor incididunt ut labore et dolore magna aliqua.</p><a>Read More</a></div>
  <div class="date"><div class="d">25 DEC</div><div class="c"><svg width="12" height="10" viewBox="0 0 12 10" fill="none" stroke="#fff" stroke-width="1.5"><path d="M1 5a5 4 0 1110 0 5 4 0 01-7 3.5L1 9.5z"/></svg>0</div></div></div>
</article>
<article class="abs news" style="left:755px">
  <div class="news-img" style="background:linear-gradient(135deg,#4d7a3c,#8fb56a 50%,#3f5fa0)" role="img" aria-label="Volunteers planting in a park"></div>
  <div class="news-row"><div><h4>Sed ut perspiciatis unde omnis iste natus</h4><p>Lorem ipsum dolor sit amet, consectetur adipiscing elit, sed do eiusmod tempor incididunt ut labore et dolore magna aliqua.</p><a>Read More</a></div>
  <div class="date"><div class="d">5 JAN</div><div class="c"><svg width="12" height="10" viewBox="0 0 12 10" fill="none" stroke="#fff" stroke-width="1.5"><path d="M1 5a5 4 0 1110 0 5 4 0 01-7 3.5L1 9.5z"/></svg>0</div></div></div>
</article>

<!-- PARTNERS -->
<h2 class="section-title" style="top:2782px"><span class="hl">DONATIONS</span> PARTNER</h2>
<div class="abs partner" style="left:174px"><i></i></div>
<div class="abs partner" style="left:393px"><i></i></div>
<div class="abs partner" style="left:611px"><i></i></div>
<div class="abs partner" style="left:829px"><i></i></div>
<div class="abs p-arrow" style="left:568px"><svg width="12" height="10" viewBox="0 0 12 10" fill="none" stroke="#333" stroke-width="1.5"><path d="M6 1L2 5l4 4M10 1L6 5l4 4"/></svg></div>
<div class="abs p-arrow" style="left:607px"><svg width="12" height="10" viewBox="0 0 12 10" fill="none" stroke="#333" stroke-width="1.5"><path d="M2 1l4 4-4 4M6 1l4 4-4 4"/></svg></div>

<!-- ASK -->
<section class="abs ask" role="img" aria-label="Volunteers background photo, darkened"></section>
<div class="dark">
  <h2 class="section-title" style="top:3012px"><span class="hl">ASK YOU</span> QUESTION</h2>
  <p class="section-sub" style="top:3062px">Sed ut perspiciatis unde omnis iste natus error sit voluptatem accusantium doloremque laudantium</p>
</div>
<div class="abs field" style="left:352px;top:3100px">First Name</div>
<div class="abs field" style="left:607px;top:3100px">Last Name</div>
<div class="abs field" style="left:352px;top:3146px">Email</div>
<div class="abs field" style="left:607px;top:3146px">Phone</div>
<div class="abs field wide" style="left:352px;top:3193px">Message</div>
<div class="abs submit">SUBMIT</div>

<!-- FOOTER -->
<footer class="abs footer"></footer>
<div class="abs f-logo"><span class="logo-mark"></span><span class="logo-name">Willowmere<br>Perks</span></div>
<div class="abs f-links">Home<span class="sep">/</span>About Us<span class="sep">/</span>Causes<span class="sep">/</span>Event<span class="sep">/</span>Blog<span class="sep">/</span>Contact Us</div>
<div class="abs f-info" style="left:396px;width:150px"><svg width="14" height="18" viewBox="0 0 14 18" fill="none" stroke="#fff" stroke-width="1.4"><path d="M7 17s6-6 6-10A6 6 0 001 7c0 4 6 10 6 10z"/><circle cx="7" cy="7" r="2"/></svg>12 Alder Row,<br>Eastbrook, FL 22900.</div>
<div class="abs f-info" style="left:555px;width:105px"><svg width="16" height="16" viewBox="0 0 16 16" fill="none" stroke="#fff" stroke-width="1.4"><path d="M3 1h3l1.5 4-2 1.2a9 9 0 004.3 4.3L11 8.5l4 1.5v3a2 2 0 01-2 2A12 12 0 011 3a2 2 0 012-2z"/></svg>1-900-555-0142</div>
<div class="abs f-info" style="left:676px;width:105px"><svg width="14" height="17" viewBox="0 0 14 17" fill="none" stroke="#fff" stroke-width="1.4"><rect x="1" y="5" width="12" height="11" rx="1"/><path d="M4 5V1h6v4M4 9h2M8 9h2M4 12h2M8 12h2"/></svg>1-900-555-0142</div>
<div class="abs f-bottom">
  <span class="mail-pill"><svg width="13" height="10" viewBox="0 0 13 10" fill="none" stroke="#fff" stroke-width="1.2"><rect x=".6" y=".6" width="11.8" height="8.8"/><path d="M.6.6l5.9 5 5.9-5"/></svg>hello@willowmereperks.org</span>
  <span class="soc"><i></i></span><span class="soc"><i></i></span><span class="soc"><i></i></span><span class="soc"><i></i></span>
</div>
<div class="abs copy">Copyright © 2020 WillowmerePerks - All Right Reserved.</div>

</body>
</html>
```